LOS PINOS DE ARENA - EXCLUSIVE AND LUXURY REAL ESTATE PROJECT

Se trata del diseño de un mono poste grande (4 m x 2 m) o (8m x 3m) anunciando la construcción de 30 villas de lujo en un terreno en primera línea de playa en el sur de España (Cádiz).

La idea es crear expectación y transmitir lujo y exclusividad.

Target Market(s)

Clientes de alto poder adquisitivo que quieran adquirir su segunda vivienda en un entorno privilegiado a escasos pasos de una de las playas más bonitas de Cádiz.

Industry/Entity Type

REAL ESTATE

Colors

Designer to choose colors to be used in the design.

Requirements
Must have
• LOS PINOS DE ARENA as the name of the development
Nice to have
• Crear expectación con ideas del tipo: “Coming soon” o “No te lo puedes perder”

```html
<!DOCTYPE html>
<html lang="es">
<head>
<meta charset="UTF-8">
<title>Los Pinos de Arena – Coming Soon</title>
<link href="https://fonts.googleapis.com/css2?family=Kaushan+Script&family=Montserrat:wght@500;700&family=Federo&display=swap" rel="stylesheet">
<style>
  :root {
    --backdrop: #ebebeb;
    --sunset-orange: #d27c30;
    --sand-peach: #d9a070;
    --sky-light: #c4e0f6;
    --sky-mid: #98c8ee;
    --navy: #0c1f78;
    --ocean-blue: #1b98d6;
    --ink: #1d1d1f;
    --terracotta: #d4835c;
    --white: #ffffff;
  }
  * { margin: 0; padding: 0; box-sizing: border-box; }
  html, body {
    width: 1200px; height: 600px; overflow: hidden;
    background: var(--backdrop);
  }
  .billboard {
    position: absolute; left: 50px; top: 88px;
    width: 1100px; height: 424px;
    box-shadow: 0 2px 6px rgba(0,0,0,.25);
    overflow: hidden;
  }
  .billboard__shapes { position: absolute; inset: 0; }
  .headline {
    position: absolute; left: 56px; top: 62px;
    width: 520px; overflow: hidden;
    padding: 0 0 14px 10px;
    font-family: "Kaushan Script", cursive;
    font-size: 96px; line-height: 1.15;
    color: var(--navy);
    transform: rotate(-4deg);
    transform-origin: left center;
    text-shadow: -7px 9px 0 var(--ocean-blue);
    white-space: nowrap;
  }
  .offer {
    position: absolute; left: 90px; top: 250px; width: 380px;
    text-align: center; color: var(--ink);
  }
  .offer__icon { display: block; margin: 0 auto; }
  .offer__title {
    font-family: "Montserrat", sans-serif; font-weight: 700;
    font-size: 36px; letter-spacing: 0.5px; line-height: 1.1;
    margin-top: 2px;
  }
  .offer__place {
    font-family: "Montserrat", sans-serif; font-weight: 500;
    font-size: 13px; letter-spacing: 10px; margin-top: 8px;
    padding-left: 10px;
  }
  .offer__rule {
    width: 165px; height: 2px; background: var(--ink);
    margin: 10px auto 0;
  }
  .development-name {
    position: absolute; right: 22px; bottom: 18px;
    font-family: "Federo", sans-serif; font-size: 28px;
    color: var(--white); letter-spacing: 1px;
    white-space: nowrap;
  }
</style>
</head>
<body>
  <div class="billboard">
    <svg class="billboard__shapes" width="1100" height="424" viewBox="0 0 1100 424">
      <defs>
        <linearGradient id="sunsetSky" x1="0" y1="0" x2="0" y2="1">
          <stop offset="0" stop-color="var(--sunset-orange)"/>
          <stop offset="0.3" stop-color="var(--sand-peach)"/>
          <stop offset="0.55" stop-color="var(--sky-light)"/>
          <stop offset="1" stop-color="var(--sky-mid)"/>
        </linearGradient>
        <linearGradient id="villaPhoto" x1="0" y1="0" x2="0" y2="1">
          <stop offset="0" stop-color="#4a78c2"/>
          <stop offset="0.35" stop-color="#cfd8e4"/>
          <stop offset="0.7" stop-color="#c9c2ae"/>
          <stop offset="1" stop-color="#8e7a66"/>
        </linearGradient>
      </defs>
      <rect class="panel-left" width="1100" height="424" fill="url(#sunsetSky)"/>
      <polygon class="photo-area" points="590,0 1100,0 1100,424 668,424" fill="url(#villaPhoto)" role="img" aria-label="Fotografía de villas modernas blancas con terraza y piscina bajo cielo azul"/>
      <polygon class="corner-band" points="668,424 1100,296 1100,424" fill="var(--terracotta)"/>
      <g class="accent-lines" stroke="var(--white)" stroke-width="2.5" fill="none">
        <line x1="596" y1="78" x2="623" y2="262"/>
        <line x1="620" y1="44" x2="648" y2="266"/>
        <line x1="772" y1="368" x2="1020" y2="306"/>
        <line x1="924" y1="358" x2="1073" y2="315"/>
      </g>
    </svg>

    <div class="headline">Coming Soon</div>

    <div class="offer">
      <svg class="offer__icon" width="170" height="32" viewBox="0 0 170 32" fill="none" stroke="var(--ink)" stroke-width="2">
        <line x1="0" y1="28" x2="48" y2="28"/>
        <line x1="122" y1="28" x2="170" y2="28"/>
        <path d="M70 28 a15 15 0 0 1 30 0"/>
        <line x1="62" y1="28" x2="108" y2="28"/>
        <line x1="85" y1="2" x2="85" y2="9"/>
        <line x1="70" y1="7" x2="74" y2="13"/>
        <line x1="100" y1="7" x2="96" y2="13"/>
        <line x1="61" y1="17" x2="67" y2="20"/>
        <line x1="109" y1="17" x2="103" y2="20"/>
      </svg>
      <div class="offer__title">30 VILLAS DE LUJO</div>
      <div class="offer__place">EN PLAYA DE CADIZ</div>
      <div class="offer__rule"></div>
    </div>

    <div class="development-name">LOS PINOS DE ARENA</div>
  </div>
</body>
</html>
```